Sympathy Gift Supplier needs packaging designs

We provide sympathy/bereavement gifts such as memorial candles and picture frames for those who recently lost a loved one. We need packaging design for our boxes that will be uplifting and positive, yet elegant.

We have attached our logo in white and black as well as a saying we would like on the box, and what we need on the back panel.
Ignore the black as it was something we were working on for another product.

Target Market(s)

These products will be given as gifts to people who lost a loved one as remembrance.

Requirements
Must have
• Back panel details (provided)
Memorial quote (provided)
Must be appropriate for this type of product

```html
<!DOCTYPE html>
<html lang="en">
<head>
<meta charset="utf-8">
<title>Serene Grove – Memorial Candle Box Dieline</title>
<link rel="stylesheet" href="https://fonts.googleapis.com/css2?family=Roboto+Condensed:wght@400;700&family=Parisienne&family=Roboto:wght@300&display=swap">
<style>
  :root {
    --paper: #ffffff;
    --ink-line: #111111;
    --brand-purple: #5b3cb1;
    --brand-green: #8cc43e;
    --label-grey: #c8c8c8;
    --label-dark: #3a2a6e;
    --leaf-white: #ffffff;
  }
  html, body {
    margin: 0;
    padding: 0;
    width: 776px;
    height: 1200px;
    overflow: hidden;
    background: var(--paper);
  }
  .dieline {
    display: block;
    width: 776px;
    height: 1200px;
  }
  .cut-line { fill: none; stroke: var(--ink-line); stroke-width: 2; }
  .flap { fill: var(--paper); stroke: var(--ink-line); stroke-width: 2; }
  .band-purple { fill: var(--brand-purple); }
  .band-green { fill: var(--brand-green); }
  .panel-label {
    font-family: "Roboto", sans-serif;
    font-weight: 300;
    font-size: 46px;
    fill: var(--label-grey);
  }
  .panel-label--bottom { fill: var(--label-dark); opacity: .75; font-size: 48px; }
  .panel-label--side { fill: var(--paper); opacity: .18; font-size: 40px; }
  .brand-name {
    font-family: "Roboto Condensed", sans-serif;
    font-weight: 700;
    font-size: 34px;
    fill: var(--brand-purple);
  }
  .brand-mark { fill: var(--brand-green); }
  .memorial-quote {
    font-family: "Parisienne", cursive;
    font-size: 24px;
    fill: var(--brand-purple);
  }
  .back-copy {
    font-family: "Roboto Condensed", sans-serif;
    font-weight: 700;
    font-size: 11.5px;
    fill: var(--brand-purple);
  }
  .back-copy--heading { fill: var(--brand-green); font-size: 13px; }
  .back-copy--mission { font-size: 13px; }
  .back-copy--web { fill: var(--brand-green); font-size: 15px; }
</style>
</head>
<body>
<svg class="dieline" viewBox="0 0 1552 2400" xmlns="http://www.w3.org/2000/svg">
  <defs>
    <linearGradient id="tree-purple" x1="0" y1="0" x2="1" y2="1">
      <stop offset="0" stop-color="#8d78cf"/>
      <stop offset="1" stop-color="#6e54bd"/>
    </linearGradient>
    <linearGradient id="tree-green" x1="1" y1="0" x2="0" y2="1">
      <stop offset="0" stop-color="#b4da80"/>
      <stop offset="1" stop-color="#9dce5a"/>
    </linearGradient>
  </defs>

  <!-- top panel and flaps -->
  <g class="box-top">
    <polygon class="flap" points="620,215 905,215 988,298 537,298"/>
    <polygon class="flap" points="537,298 447,390 447,688 537,760"/>
    <polygon class="flap" points="988,298 1083,393 1082,686 988,760"/>
    <rect class="cut-line" x="537" y="298" width="451" height="462"/>
    <g transform="rotate(180 757 462)">
      <circle class="brand-mark" cx="660" cy="450" r="9"/>
      <text class="brand-name" x="682" y="462">Serene Grove</text>
    </g>
    <g class="memorial-quote" text-anchor="middle" transform="rotate(180 762 620)">
      <text x="762" y="580">When the people we love</text>
      <text x="762" y="608">are taken away from us,</text>
      <text x="762" y="636">the way to have them live on</text>
      <text x="762" y="664">is to never stop loving them.</text>
    </g>
    <text class="panel-label" x="1140" y="494">TOP</text>
  </g>

  <!-- back panel and flaps -->
  <g class="box-back">
    <polygon class="flap" points="537,760 445,852 445,1138 537,1222"/>
    <polygon class="flap" points="988,760 1080,852 1084,1140 988,1222"/>
    <rect class="cut-line" x="537" y="760" width="451" height="462"/>
    <g text-anchor="middle">
      <text class="back-copy back-copy--heading" x="762" y="812">WARNING</text>
      <text class="back-copy" x="762" y="826">Burn within sight. Keep away from flammable objects.</text>
      <text class="back-copy" x="762" y="840">Keep away from children and pets.</text>
      <text class="back-copy" x="762" y="868">BURNING INSTRUCTIONS</text>
      <text class="back-copy" x="762" y="882">Trim wick to 1/4" before lighting.  Keep candle free of any</text>
      <text class="back-copy" x="762" y="896">foreign materials including matches and wick trimmings.</text>
      <text class="back-copy" x="762" y="910">Only burn the candle on a level, fire resistant surface.</text>
      <text class="back-copy" x="762" y="924">Do not burn candle for more than four hours at a time.  Stop</text>
      <text class="back-copy" x="762" y="938">use when only 1/4" of wax remains.</text>
      <text class="back-copy" x="762" y="966">MADE IN CHINA.</text>
      <path d="M742 995 q20 -12 40 0" fill="none" stroke="var(--brand-green)" stroke-width="4" stroke-linecap="round"/>
      <text class="back-copy back-copy--mission" x="762" y="1033">SERENE GROVE IS A FAMILY OWNED COMPANY</text>
      <text class="back-copy back-copy--mission" x="762" y="1050">AND ALL OF OUR PRODUCTS ARE CAREFULLY DESIGNED</text>
      <text class="back-copy back-copy--mission" x="762" y="1067">AND CRAFTED WITH YOUR FAMILY IN MIND.</text>
      <circle class="brand-mark" cx="688" cy="1133" r="8"/>
      <text class="brand-name" x="770" y="1145" style="font-size:28px">Serene Grove</text>
      <text class="back-copy back-copy--web" x="762" y="1196">www.SereneGrove.com</text>
    </g>
    <text class="panel-label" x="1120" y="1016">BACK</text>
  </g>

  <!-- colour band: side, bottom, side -->
  <g class="box-band">
    <rect class="band-purple" x="56" y="1210" width="481" height="485"/>
    <rect class="band-green" x="988" y="1210" width="485" height="485"/>
    <polygon class="band-purple" points="537,1222 988,1222 537,1682"/>
    <polygon class="band-green" points="988,1222 988,1682 537,1682"/>
    <rect role="img" aria-label="White leafy tree branch silhouette reaching in from the right" x="64" y="1210" width="484" height="485" fill="url(#tree-purple)" opacity="0.55"/>
    <rect role="img" aria-label="White leafy tree branch silhouette reaching in from the left" x="976" y="1210" width="484" height="485" fill="url(#tree-green)" opacity="0.6"/>
    <rect class="cut-line" x="70" y="1222" width="1386" height="460"/>
    <line class="cut-line" x1="537" y1="1222" x2="537" y2="1682"/>
    <line class="cut-line" x1="988" y1="1222" x2="988" y2="1682"/>
    <text class="panel-label panel-label--bottom" x="763" y="1474" text-anchor="middle">BOTTOM</text>
    <text class="panel-label panel-label--side" transform="rotate(-90 300 1410)" x="300" y="1410" text-anchor="middle">SIDE</text>
  </g>

  <!-- front panel and flaps -->
  <g class="box-front">
    <polygon class="flap" points="537,1682 453,1766 453,2064 537,2148"/>
    <polygon class="flap" points="988,1682 1083,1774 1083,2064 988,2148"/>
    <rect class="cut-line" x="537" y="1682" width="451" height="466"/>
    <g transform="rotate(180 757 1912)">
      <circle class="brand-mark" cx="660" cy="1900" r="9"/>
      <text class="brand-name" x="682" y="1912">Serene Grove</text>
    </g>
    <text class="panel-label" x="1106" y="1944">FRONT</text>
  </g>
</svg>
</body>
</html>
```